Financial Services Business Card Design

We are a financial services company Based in London, offering Short term Funding Solutions for companies, raising anywhere between £20,000 and £25million pounds.

The Card must have a professional look as it is going to be handed out to professionals I.E Solicitors, Accountants, Company directors and Business owners.

See Attached our company Logo

Industry/Entity Type

Business

Contact Information for Business Card

Brett Kolvane
Suite 41
R T House
Hazelbrook Lane
Watford
WD17 4QL

```html
<!DOCTYPE html>
<html lang="en">
<head>
<meta charset="utf-8">
<title>Northvale Capital – Business Card</title>
<link rel="stylesheet" href="https://fonts.googleapis.com/css2?family=Arimo:wght@400;700&display=swap">
<style>
  :root {
    --page-bg: #e9e7e3;
    --card-white: #f4f4f4;
    --card-black: #050505;
    --brand-green: #3aab4b;
    --brand-blue: #2f7fc4;
    --ink: #111111;
    --paper-white: #ffffff;
    --frame: 8px;
  }
  * { box-sizing: border-box; margin: 0; padding: 0; }
  html, body {
    width: 1200px;
    height: 864px;
    overflow: hidden;
  }
  body {
    background: var(--page-bg);
    font-family: "Arimo", Arial, sans-serif;
    display: flex;
    align-items: center;
    justify-content: center;
    gap: 40px;
  }
  .card {
    position: relative;
    width: 530px;
    height: 303px;
    box-shadow: 0 6px 18px rgba(0,0,0,0.18);
    overflow: hidden;
  }
  .card--front { background: var(--card-white); }
  .card--back { background: var(--card-black); }

  /* two-tone frame: green along top and upper right, blue along bottom and lower left */
  .frame-edge { position: absolute; }
  .frame-edge--top { top: 0; left: 0; right: 0; height: var(--frame); background: var(--brand-green); }
  .frame-edge--bottom { bottom: 0; left: 0; right: 0; height: var(--frame); background: var(--brand-blue); }
  .frame-edge--left {
    top: 0; bottom: 0; left: 0; width: var(--frame);
    background: linear-gradient(to bottom, var(--brand-green) 0 28%, var(--brand-blue) 28% 100%);
  }
  .frame-edge--right {
    top: 0; bottom: 0; right: 0; width: var(--frame);
    background: linear-gradient(to bottom, var(--brand-green) 0 80%, var(--brand-blue) 80% 100%);
  }

  /* front face */
  .front-content {
    position: absolute;
    inset: var(--frame);
    display: flex;
    flex-direction: column;
    align-items: center;
    padding: 40px 24px 0;
  }
  .brand-lockup {
    display: flex;
    align-items: center;
    gap: 12px;
  }
  .brand-mark {
    width: 20px;
    height: 20px;
    border-radius: 50%;
    background: var(--brand-green);
    flex: none;
  }
  .brand-name {
    font-weight: 700;
    font-size: 34px;
    letter-spacing: 1px;
    color: var(--brand-blue);
    text-transform: uppercase;
    white-space: nowrap;
  }
  .divider {
    width: 400px;
    height: 2px;
    background: var(--ink);
    margin: 18px 0 16px;
  }
  .holder-name {
    font-size: 28px;
    font-weight: 400;
    color: var(--brand-green);
    margin-bottom: 12px;
    white-space: nowrap;
  }
  .contact-line {
    font-size: 15px;
    color: var(--ink);
    line-height: 1.4;
    text-align: center;
    white-space: nowrap;
  }

  /* back face */
  .back-content {
    position: absolute;
    inset: var(--frame);
    display: flex;
    align-items: center;
    justify-content: center;
    padding: 0 30px;
  }
  .back-wordmark {
    font-weight: 700;
    font-size: 40px;
    letter-spacing: 1px;
    color: var(--paper-white);
    text-transform: uppercase;
    text-align: center;
    white-space: nowrap;
  }
</style>
</head>
<body>
  <section class="card card--front" aria-label="Business card front">
    <span class="frame-edge frame-edge--top"></span>
    <span class="frame-edge frame-edge--right"></span>
    <span class="frame-edge frame-edge--bottom"></span>
    <span class="frame-edge frame-edge--left"></span>
    <div class="front-content">
      <div class="brand-lockup">
        <span class="brand-mark"></span>
        <span class="brand-name">Northvale Capital</span>
      </div>
      <div class="divider"></div>
      <p class="holder-name">Brett Kolvane</p>
      <p class="contact-line">020-946-3218</p>
      <p class="contact-line">brett@northvalecapital.com</p>
      <p class="contact-line">Suite 41, R T House, Hazelbrook Lane, Watford, WD17 4QL</p>
    </div>
  </section>

  <section class="card card--back" aria-label="Business card back">
    <span class="frame-edge frame-edge--top"></span>
    <span class="frame-edge frame-edge--right"></span>
    <span class="frame-edge frame-edge--bottom"></span>
    <span class="frame-edge frame-edge--left"></span>
    <div class="back-content">
      <span class="back-wordmark">Northvale Capital</span>
    </div>
  </section>
</body>
</html>
```